www.tilbrookhealth.com

We are a company that is in the business of extending the life of surgical equipment by repairing or refurbishing equipment to save hospitals, surgery centers and clinics money. We call ourselves Tilbrook Medical Corporation. We are in need of a website that delivers the "feel" of what of we do everyday. A website that explains our services but at the same time has a touch that is different from the rest. Many companies repair but their websites may not "pull" customers to inquire, we need that punch. At this time we are not looking for e-commerce but would like the option of adding that in the future. We do sell new and used equipment, so we like to be able to highlight those manufacturers on our site. We would like the website to have enough layouts for pictures to describe what we repair.
Target Market(s)
Biomedical Technicians and Managers, Hospital Purchasing Departments, OR Managers, type of facilities that our customer exists in, hospitals, surgery centers, clinics, animal hospitals
Industry/Entity Type
E-Commerce
Requirements
Must have
- An easy to navigate website, modern looking.
Easy to modify with pictures and or additional web pages
The winning designer to be available for future modifications and changes
Website to be unique compared to our competition, which are numerous
Nice to have
- E-Commerce capability

```html
<!DOCTYPE html>
<html lang="en">
<head>
<meta charset="utf-8">
<title>Tilbrook Medical Corporation</title>
<link href="https://fonts.googleapis.com/css2?family=Arimo:wght@400;700&family=Cinzel:wght@400;700&family=Oswald:wght@500&display=swap" rel="stylesheet">
<style>
:root{
  --ink:#222;
  --muted:#777;
  --brand:#2f5a8a;
  --blue:#2aa3d8;
  --navy:#36486b;
  --black:#1b1b1b;
  --line:#d8d8d8;
  --band:#dcdcdc;
  --panel:#eeeeee;
  --star:#5b62a8;
  --red:#b3282d;
  --white:#fff;
}
*{box-sizing:border-box;margin:0;padding:0}
html,body{width:843px;height:1200px;overflow:hidden;background:var(--white)}
body{position:relative;font-family:"Arimo",Arial,sans-serif;color:var(--ink)}
.abs{position:absolute}

.logo{left:89px;top:30px;font-size:24px;letter-spacing:1px;color:var(--brand)}
.search{left:612px;top:36px;width:214px;height:20px;border:1px solid var(--line);display:flex;align-items:center}
.search-btn{width:22px;height:20px;background:#555;display:flex;align-items:center;justify-content:center;margin-left:-1px}
.search-text{font-size:8px;color:var(--muted);padding-left:6px}

.nav{left:89px;top:100px;width:700px;height:32px}
.nav-item{position:absolute;top:0;font-size:9.5px;font-weight:700;transform:translateX(-50%);white-space:nowrap}
.nav-home{left:15px;top:-2px}
.nav-rule{left:89px;top:131px;width:700px;height:1px;background:var(--line)}
.nav-active{left:147px;top:130px;width:50px;height:2px;background:var(--blue)}

.quick-search{left:89px;top:138px;width:145px;height:233px;background:var(--panel)}
.qs-head{height:22px;background:var(--black);color:#fff;font-family:"Cinzel",serif;font-weight:700;font-size:11px;display:flex;align-items:center;justify-content:center}
.qs-label{font-size:6.5px;margin:6px 0 0 6px;font-weight:700}
.qs-radio{font-size:6.5px;margin:4px 0 0 6px;display:flex;gap:8px;align-items:center}
.dot{display:inline-block;width:7px;height:7px;border:1px solid #888;border-radius:50%;vertical-align:middle;margin-right:2px;background:#fff}
.dot.on{background:radial-gradient(#333 40%,#fff 45%)}
.qs-select{margin:4px 6px 0;height:14px;background:#fff;border:1px solid #ccc;font-size:6px;padding:3px 4px;position:relative}
.qs-select::after{content:"";position:absolute;right:5px;top:4px;border-left:4px solid #333;border-top:3px solid transparent;border-bottom:3px solid transparent}
.qs-loc{display:flex;gap:3px;margin:4px 6px 0;font-size:6px;align-items:center}
.qs-loc span.box{background:#fff;border:1px solid #ccc;height:13px;padding:2px 3px;flex:1}

.hero{left:258px;top:138px;width:339px;height:267px;background:linear-gradient(150deg,#9fb3c9,#3f5f86 55%,#5a7ca3)}
.tag{position:absolute;font-family:"Oswald",sans-serif;letter-spacing:1px;color:#334;background:rgba(230,236,244,.7);padding:1px 6px}
.tag-repair{left:28px;top:16px;font-size:19px;color:#2c3c55}
.tag-equip{left:135px;top:46px;font-size:10px;color:#2aa3d8;background:rgba(200,215,235,.6)}
.tag-save{left:200px;top:68px;font-size:10px;color:#333}

.pager{left:258px;top:413px;width:339px;height:34px;border:1px solid #ccc;display:flex;align-items:center;justify-content:space-between}
.pager-arrow{width:54px;height:34px;background:var(--black);display:flex;align-items:center;justify-content:center}
.pager-nums{font-family:"Cinzel",serif;font-size:15px;display:flex;gap:12px}
.pager-nums .cur{color:var(--navy)}

.ad{left:620px;top:162px;width:132px;height:286px;border:1px solid #ccc;text-align:center}
.ad-head{font-size:11px;font-weight:700;margin-top:18px}
.ad-head b{color:var(--blue)}
.ad-visual{position:absolute;left:8px;top:48px;width:44px;height:110px;background:linear-gradient(160deg,#cfcfcf,#7c7c7c)}
.ad-the{position:absolute;left:58px;top:84px;font-family:"Oswald",sans-serif;color:var(--navy);font-size:18px}
.ad-best{position:absolute;left:92px;top:88px;font-size:7px;color:var(--muted)}
.ad-price{position:absolute;left:58px;top:106px;font-family:"Oswald",sans-serif;color:var(--blue);font-size:22px}
.ad-badge{position:absolute;left:98px;top:138px;width:26px;height:26px;border-radius:50%;background:var(--blue);color:#fff;font-size:6px;display:flex;align-items:center;justify-content:center}
.ad-offer{position:absolute;left:14px;top:184px;font-size:7px;color:var(--muted)}
.ad-order{position:absolute;left:76px;top:198px;font-size:6px;color:var(--blue)}
.ad-foot{position:absolute;left:0;width:100%;top:244px;font-family:"Oswald",sans-serif;font-size:10px}

.freecall{left:92px;top:413px;width:140px;height:34px;display:flex;align-items:center;gap:8px}
.freecall-text{font-size:10px;line-height:1.2}
.freecall-text .free{color:var(--star);font-weight:700}
.freecall-text .num{font-size:12px;font-weight:700}
.freecall-rule{left:89px;top:450px;width:142px;height:2px;background:var(--blue)}

.quick-menu{left:89px;top:467px;width:142px;height:162px}
.qm-head{height:39px;background:var(--navy);color:#fff;font-family:"Cinzel",serif;font-size:13px;display:flex;align-items:center;justify-content:center}
.qm-item{height:41px;border:1px solid #ccc;border-top:none;display:flex;align-items:center;justify-content:space-between;padding:0 12px 0 30px;font-size:9px;color:#555}
.qm-arrow{border-left:6px solid var(--blue);border-top:4px solid transparent;border-bottom:4px solid transparent}

.testi-icon{left:255px;top:486px;width:40px;height:40px;border-radius:50%;background:var(--blue)}
.testi-title{left:380px;top:500px;width:150px;text-align:center;font-size:20px;letter-spacing:.5px}
.testi-more{left:733px;top:498px}
.testi-rule{left:250px;top:535px;width:540px;height:1px;background:#eee}
.testi-quote{left:250px;top:553px;width:540px;font-size:10.5px;line-height:1.5;color:#333}

.band-rule{left:67px;top:654px;width:725px;height:4px;background:var(--blue)}
.band-pointer{left:425px;top:657px;border-left:8px solid transparent;border-right:8px solid transparent;border-top:8px solid var(--blue)}
.band{left:67px;top:658px;width:725px;height:205px;background:var(--band)}
.band-title{left:67px;top:692px;width:725px;text-align:center;font-size:16px;letter-spacing:.5px}

.card{position:absolute;top:738px;width:146px;height:135px;background:#fff;border:1px solid #ccc}
.card-photo{position:absolute;left:30px;top:8px;width:86px;height:64px;background:linear-gradient(#f4f4f4,#c8c8c8)}
.card-caption{position:absolute;left:12px;top:96px;font-size:6.5px;font-weight:700;white-space:nowrap}
.card-stars{position:absolute;left:70px;top:110px;display:flex;gap:3px}

.faq-rule{top:917px;height:1px;background:#aaa}
.faq-icon{left:432px;top:906px}
.faq-title{left:330px;top:943px;width:200px;text-align:center;font-family:"Oswald",sans-serif;font-size:20px}
.faq-title small{font-size:12px;color:var(--navy)}
.faq-title-rule{left:360px;top:974px;width:140px;height:1px;background:#ccc}
.faq-card{position:absolute;top:998px;width:146px;height:98px;background:#fff;border:1px solid #ddd;box-shadow:0 1px 3px rgba(0,0,0,.15);padding:8px 7px}
.faq-q{font-family:"Cinzel",serif;font-size:10.5px;line-height:1.25;color:#333}
.faq-q b{color:var(--red);font-weight:400}
.faq-a{position:absolute;right:8px;bottom:6px;font-size:8px}

.foot-rule{left:98px;width:645px;height:1px;background:#aaa}
.have-more{left:663px;top:1115px;font-size:12px;text-decoration:underline}
.have-more-dot{left:722px;top:1113px;width:17px;height:17px;border-radius:50%;background:var(--blue);color:#fff;font-size:11px;font-weight:700;display:flex;align-items:center;justify-content:center}
.social{left:666px;top:1135px;display:flex;gap:6px}
.social span{width:7px;height:7px;border-radius:50%;background:#333}
.copyright{left:327px;top:1136px;font-size:7px}
</style>
</head>
<body>

<div class="abs logo">TILBROOK</div>
<div class="abs search">
  <div class="search-btn"><svg width="10" height="10" viewBox="0 0 10 10"><circle cx="4" cy="4" r="3" fill="none" stroke="#fff" stroke-width="1.5"/><line x1="6" y1="6" x2="9" y2="9" stroke="#fff" stroke-width="1.5"/></svg></div>
  <span class="search-text">search entire store here...</span>
</div>

<nav class="abs nav">
  <svg class="nav-item nav-home" width="10" height="10" viewBox="0 0 10 10"><path d="M5 0 L10 5 H8.5 V10 H1.5 V5 H0 Z" fill="var(--blue)"/></svg>
  <span class="nav-item" style="left:83px;color:var(--brand)">HOME</span>
  <span class="nav-item" style="left:172px">FREE QUOTE</span>
  <span class="nav-item" style="left:260px">SERVICES</span>
  <span class="nav-item" style="left:349px">FAQ</span>
  <span class="nav-item" style="left:439px">MANUFACTURERS</span>
  <span class="nav-item" style="left:527px">CONTACT US</span>
  <span class="nav-item" style="left:614px">ABOUT US</span>
</nav>
<div class="abs nav-rule"></div>
<div class="abs nav-active"></div>

<aside class="abs quick-search">
  <div class="qs-head">QUICK SEARCH</div>
  <div class="qs-label">Equipment Working Condition :</div>
  <div class="qs-radio"><span><i class="dot on"></i>Yes</span><span><i class="dot"></i>No</span></div>
  <div class="qs-label">Service Preferences :</div>
  <div class="qs-radio"><span><i class="dot on"></i>Repair</span><span><i class="dot"></i>Refurbish</span></div>
  <div class="qs-select" style="margin-top:8px">Select Equipment Manufacturer</div>
  <div class="qs-select">Select Equipment Model</div>
  <div class="qs-label">Pick Up Location :</div>
  <div class="qs-loc"><span class="box">Zip</span>OR<span class="box">City</span><span class="box">St</span></div>
  <div class="qs-label">Return Location :</div>
  <div class="qs-loc"><span class="box">Zip</span>OR<span class="box">City</span><span class="box">St</span></div>
</aside>

<section class="abs hero" role="img" aria-label="Close-up photo of surgical equipment being repaired">
  <span class="tag tag-repair">REPAIRING</span>
  <span class="tag tag-equip">EQUIPMENTS</span>
  <span class="tag tag-save">SAVE YOUR MONEY</span>
</section>

<div class="abs pager">
  <div class="pager-arrow"><svg width="8" height="8" viewBox="0 0 8 8"><path d="M8 0 V8 L0 4 Z" fill="#fff"/></svg></div>
  <div class="pager-nums"><span>1</span><span class="cur">2</span><span>3</span><span>4</span><span>5</span><span>6</span></div>
  <div class="pager-arrow"><svg width="8" height="8" viewBox="0 0 8 8"><path d="M0 0 V8 L8 4 Z" fill="#fff"/></svg></div>
</div>

<aside class="abs ad">
  <div class="ad-head">OUR <b>USED</b> STORE</div>
  <div class="ad-visual" role="img" aria-label="Photo of a stethoscope"></div>
  <span class="ad-the">THE</span>
  <span class="ad-best">BEST</span>
  <span class="ad-price">PRICE</span>
  <span class="ad-badge">TRY</span>
  <span class="ad-offer">This offer till 30-08-2013</span>
  <span class="ad-order">order now</span>
  <div class="ad-foot">PARTNER PAID ADV</div>
</aside>

<div class="abs freecall">
  <svg width="26" height="16" viewBox="0 0 26 16"><path d="M0 4 H18 M0 12 H18 M14 0 L22 8 L14 16" fill="none" stroke="#222" stroke-width="2"/></svg>
  <div class="freecall-text"><div class="free">FREE</div><div class="num">555-014-2290</div></div>
</div>
<div class="abs freecall-rule"></div>

<aside class="abs quick-menu">
  <div class="qm-head">QUICK MENU</div>
  <div class="qm-item">Repair services<i class="qm-arrow"></i></div>
  <div class="qm-item">Used equipment<i class="qm-arrow"></i></div>
  <div class="qm-item">New equipment<i class="qm-arrow"></i></div>
</aside>

<div class="abs testi-icon"></div>
<h2 class="abs testi-title" style="font-weight:400">TESTIMONIALS</h2>
<svg class="abs testi-more" width="12" height="10" viewBox="0 0 12 10"><path d="M1 1 L5 5 L1 9 M6 1 L10 5 L6 9" fill="none" stroke="#333" stroke-width="1.3"/></svg>
<div class="abs testi-rule"></div>
<p class="abs testi-quote">"...thank you for the level of professionalism and care that you showed in repairing our surgical instruments. I believe that you were exceedingly understanding and forthright..."</p>

<div class="abs band"></div>
<div class="abs band-rule"></div>
<div class="abs band-pointer"></div>
<h2 class="abs band-title" style="font-weight:400">OUR HISTORY'S FEEDBACK</h2>

<svg width="0" height="0" style="position:absolute"><defs><path id="s" d="M5 0 L6.2 3.6 H10 L7 5.8 L8.1 9.5 L5 7.2 L1.9 9.5 L3 5.8 L0 3.6 H3.8 Z"/></defs></svg>

<div class="card" style="left:115px">
  <div class="card-photo" role="img" aria-label="Portrait of a customer"></div>
  <div class="card-caption">AMAZING AND GOOD</div>
  <div class="card-stars"><svg width="60" height="10"><g fill="var(--star)"><use href="#s"/><use href="#s" x="12"/><use href="#s" x="24"/><use href="#s" x="36"/><use href="#s" x="48"/></g></svg></div>
</div>
<div class="card" style="left:282px">
  <div class="card-photo" role="img" aria-label="Portrait of a customer"></div>
  <div class="card-caption">HOW CAN YOU BELIEVE</div>
  <div class="card-stars"><svg width="60" height="10"><g fill="var(--star)"><use href="#s"/><use href="#s" x="12"/><use href="#s" x="24"/><use href="#s" x="36"/><use href="#s" x="48"/></g></svg></div>
</div>
<div class="card" style="left:448px">
  <div class="card-photo" role="img" aria-label="Portrait of a customer"></div>
  <div class="card-caption">FAST AND CAREFUL REPAIRS</div>
  <div class="card-stars"><svg width="60" height="10"><g fill="var(--star)"><use href="#s"/><use href="#s" x="12"/><use href="#s" x="24"/><use href="#s" x="36"/><use href="#s" x="48"/></g></svg></div>
</div>
<div class="card" style="left:614px">
  <div class="card-photo" role="img" aria-label="Portrait of a customer"></div>
  <div class="card-caption">SAVED OUR CLINIC MONEY</div>
  <div class="card-stars"><svg width="60" height="10"><g fill="var(--star)"><use href="#s"/><use href="#s" x="12"/><use href="#s" x="24"/><use href="#s" x="36"/><use href="#s" x="48"/></g></svg></div>
</div>

<div class="abs faq-rule" style="left:98px;width:318px"></div>
<div class="abs faq-rule" style="left:445px;width:298px"></div>
<svg class="abs faq-icon" width="30" height="34" viewBox="0 0 30 34"><path d="M15 1 A13 13 0 1 1 9 26 L5 32 L8 24 A13 13 0 0 1 15 1 Z" fill="#fff" stroke="#999"/><text x="15" y="21" font-size="15" font-weight="700" text-anchor="middle" font-family="Arimo,sans-serif">!</text></svg>
<h2 class="abs faq-title" style="font-weight:500">FAQ <small>( YOU ASK)</small></h2>
<div class="abs faq-title-rule"></div>

<div class="faq-card" style="left:98px"><p class="faq-q"><b>How</b> much notice is needed to schedule repair of my equipment?</p><span class="faq-a">The answer</span></div>
<div class="faq-card" style="left:266px"><p class="faq-q"><b>What</b> is a reasonable estimate of time from request to return of my device?</p><span class="faq-a">The answer</span></div>
<div class="faq-card" style="left:430px"><p class="faq-q"><b>What</b> kind of surgical equipment do you repair?</p><span class="faq-a">The answer</span></div>
<div class="faq-card" style="left:593px"><p class="faq-q"><b>Who</b> ships my instruments to your service center and back?</p><span class="faq-a">The answer</span></div>

<div class="abs foot-rule" style="top:1110px"></div>
<a class="abs have-more" style="color:var(--ink)">have more</a>
<div class="abs have-more-dot">?</div>
<div class="abs social"><span></span><span></span><span></span><span></span><span></span></div>
<div class="abs copyright">allrights reserved by your company 2013</div>
<div class="abs foot-rule" style="top:1163px"></div>

</body>
</html>
```